Duct Manufacturing Company new to the industry needs business card and stationary design

we are sheet metal duct manufacturers looking for a business card design to fit my new business logo.
nothing to crazy that will date, but want it to stand out from the crowed.
I'm sure you guys will work it out.

Industry/Entity Type

Business

Contact Information for Business Card

Wade Collin
Director

Address
17 Paverly St
Carrowdale NSW 2714

0438 657 904

Sales@flowbend.com.au

Font styles to use
Other font styles liked:
• BankGothic md bt

Requirements
Nice to have
• Like the idea of corner rounded to match logo
• like to keep colours flowing
• font I like sharp square not rounded

```html
<!DOCTYPE html>
<html lang="en">
<head>
<meta charset="utf-8">
<title>Flowbend Industries – Business Card</title>
<link rel="stylesheet" href="https://fonts.googleapis.com/css2?family=Lato:wght@400;700;900&display=swap">
<style>
  :root {
    --bg: #8e8d8e;
    --blue-deep: #064f9b;
    --blue-mid: #0a63ad;
    --green: #6fb23a;
    --ink: #1c1c1c;
    --name-blue: #0d4fa0;
    --rule: #7f9ccc;
    --url: #b9c8e4;
  }
  * { margin: 0; padding: 0; box-sizing: border-box; }
  html, body { width: 1200px; height: 900px; overflow: hidden; }
  body {
    background: var(--bg);
    font-family: "Lato", sans-serif;
    position: relative;
  }
  .card {
    position: absolute;
    left: 290px;
    width: 620px;
    height: 354px;
    border-radius: 22px;
    overflow: hidden;
    box-shadow: 0 6px 18px rgba(0,0,0,.28);
  }
  .card--front { top: 50px; background: var(--blue-deep); }
  .card--back { top: 480px; background: var(--blue-mid); }

  .brand { display: flex; align-items: center; gap: 12px; }
  .brand__dot { width: 34px; height: 34px; border-radius: 50%; background: var(--green); flex: none; }
  .brand__name {
    font-weight: 900;
    color: var(--green);
    line-height: 1.05;
    letter-spacing: 1px;
    text-transform: uppercase;
  }
  .card--front .brand { position: absolute; left: 50%; top: 118px; transform: translateX(-50%); }
  .card--front .brand__name { font-size: 40px; }
  .card--front .brand__dot { width: 44px; height: 44px; }

  .front__footer {
    position: absolute;
    left: 40px; right: 40px; bottom: 46px;
    display: flex; align-items: center; gap: 12px;
  }
  .front__rule { flex: 1; height: 1px; background: var(--rule); }
  .front__url { color: var(--url); font-size: 16px; letter-spacing: .5px; }

  .back__art { position: absolute; inset: 0; }
  .back__brand { position: absolute; left: 90px; top: 112px; }
  .back__brand .brand__name { font-size: 30px; }

  .person { position: absolute; left: 200px; top: 232px; }
  .person__name { font-weight: 900; color: var(--name-blue); font-size: 26px; }
  .person__role { font-size: 17px; color: var(--ink); }

  .contact {
    position: absolute;
    left: 372px; top: 98px;
    list-style: none;
    font-size: 16.5px;
    color: var(--ink);
    line-height: 1.45;
  }
  .contact li { display: flex; align-items: center; gap: 8px; }
  .contact svg { width: 15px; height: 15px; flex: none; fill: var(--blue-deep); }
  .contact .url-accent { color: var(--name-blue); }
  .contact__address { margin-top: 6px; padding-left: 23px; line-height: 1.35; }
</style>
</head>
<body>

<section class="card card--front" aria-label="Card front">
  <div class="brand">
    <span class="brand__dot"></span>
    <span class="brand__name">Flowbend<br>Industries</span>
  </div>
  <div class="front__footer">
    <span class="front__rule"></span>
    <span class="front__url">www.flowbend.com.au</span>
    <span class="front__rule"></span>
  </div>
</section>

<section class="card card--back" aria-label="Card back">
  <svg class="back__art" viewBox="0 0 620 354" preserveAspectRatio="none" aria-hidden="true">
    <defs>
      <linearGradient id="swoosh" x1="0" y1="0" x2="1" y2="1">
        <stop offset="0" stop-color="#5aa33a"/>
        <stop offset="1" stop-color="#a6cc38"/>
      </linearGradient>
      <linearGradient id="field" x1="0" y1="0" x2="0" y2="1">
        <stop offset="0" stop-color="#0a56a3"/>
        <stop offset="1" stop-color="#0a80c4"/>
      </linearGradient>
    </defs>
    <rect width="620" height="354" fill="url(#field)"/>
    <path d="M0,118 C150,10 430,-20 620,250 L620,290 C520,354 380,372 260,354 C120,334 20,250 0,150 Z" fill="url(#swoosh)"/>
    <path d="M18,128 C160,30 420,10 590,262 C500,330 380,348 270,340 C140,330 46,250 18,128 Z" fill="#efefef"/>
  </svg>

  <div class="brand back__brand">
    <span class="brand__dot"></span>
    <span class="brand__name">Flowbend<br>Industries</span>
  </div>

  <div class="person">
    <p class="person__name">Wade Collin</p>
    <p class="person__role">Director</p>
  </div>

  <ul class="contact">
    <li>
      <svg viewBox="0 0 16 16"><path d="M3 1h3l1 4-2 1a9 9 0 0 0 5 5l1-2 4 1v3c0 1-1 2-2 2A13 13 0 0 1 1 3c0-1 1-2 2-2z"/></svg>
      <span>0438 657 904</span>
    </li>
    <li>
      <svg viewBox="0 0 16 16"><path d="M1 3h14v10H1z M1 3l7 6 7-6" stroke="#fff" stroke-width="1.2"/></svg>
      <span>Sales@flowbend.com.au</span>
    </li>
    <li>
      <svg viewBox="0 0 16 16"><path d="M1 2h14v9H1z M3 4v5h10V4z M6 12h4v2H6z" fill-rule="evenodd"/></svg>
      <span>www.<span class="url-accent">flowbend</span>.com.au</span>
    </li>
    <li class="contact__address"><span>17 Paverly St<br>Carrowdale NSW 2714</span></li>
  </ul>
</section>

</body>
</html>
```